An eCommerce Business Needs a Wordpress Web Design and Development

We need a website design and development for a new eCommerce business based in New York called "Velvet Orra". We sell items that are based on satisfying multi-sensory pathways of the person, as we believe that all is interconnected forming the Universal Language. All our products are made of raw natural elements from earth or the cosmos. The final design should communicate visual-perceptive pathways that produce harmonious effects and creativity.
Updates

Dear Designers, Please accept my sincere apology for my delayed response. I am currently in the midst of extensive business travelling while at the same time gathering feedback from online polling with friends as the website potential end-users. I shall get back to you by May 12 or sooner. Thank you for your understanding.

Target Market(s)

Art, fossils, minerals and numismatic collectors.

Industry/Entity Type

Online Shopping

Coding

Coded - Design and coding required

Number of Pages Required

5+ page

Font styles to use
Sans Serif
Script

Colors

Designer to choose colors to be used in the design.

Requirements
Must have
• - Simple and clean design.
• - Desktop and mobile device friendly.
• - Photos and images of string musical instruments, crystals, numismatics and cultural artefacts.
• - A blog page.
• - A check-out cart for online shopping and payment. Example: https://store.plumwick.com
• - Standard links to social media.

```html
<!DOCTYPE html>
<html lang="en">
<head>
<meta charset="utf-8">
<title>Velvet Orra</title>
<link href="https://fonts.googleapis.com/css2?family=Open+Sans:wght@400;600;700&display=swap" rel="stylesheet">
<style>
  :root {
    --brand-blue: #01518f;
    --icon-blue: #0b4f8a;
    --ink: #111111;
    --dark-button: #333333;
    --field-bg: #fafafa;
    --field-border: #cccccc;
    --white: #ffffff;
    --wood-dark: #2e2620;
    --wood-mid: #4d4036;
    --wood-light: #6a5a4c;
    --product-wood: #7a3a20;
  }
  * { box-sizing: border-box; margin: 0; padding: 0; }
  html, body { width: 1200px; height: 1000px; overflow: hidden; background: var(--white); }
  body { font-family: "Open Sans", sans-serif; color: var(--ink); position: relative; }

  .site-header { position: absolute; top: 0; left: 0; width: 1200px; height: 119px; }
  .brand-name {
    position: absolute; left: 38px; top: 28px; width: 120px;
    font-size: 28px; line-height: 32px; font-weight: 400; color: var(--brand-blue);
    letter-spacing: 2px;
  }
  .search-form { position: absolute; left: 424px; top: 39px; display: flex; }
  .search-field {
    width: 291px; height: 42px; border: 1px solid var(--field-border); background: var(--field-bg);
    font: 400 17px "Open Sans", sans-serif; color: #888; padding: 0 15px; line-height: 40px;
  }
  .search-button { width: 59px; height: 42px; background: var(--dark-button); display: flex; align-items: center; justify-content: center; }
  .account-icon { position: absolute; left: 1056px; top: 49px; }
  .cart-icon { position: absolute; left: 1114px; top: 49px; }
  .cart-count {
    position: absolute; left: 1133px; top: 40px; width: 28px; height: 24px; border-radius: 12px;
    border: 1.5px solid var(--icon-blue); background: var(--white); color: var(--ink);
    font-size: 13px; font-weight: 700; text-align: center; line-height: 21px;
  }

  .main-nav {
    position: absolute; left: 38px; top: 119px; width: 1122px; height: 66px;
    background: var(--brand-blue); display: flex; align-items: center; padding-left: 36px; gap: 36px;
  }
  .main-nav a { color: var(--white); font-size: 14.5px; text-decoration: none; display: flex; align-items: center; gap: 5px; }
  .caret { width: 0; height: 0; border-left: 4.5px solid transparent; border-right: 4.5px solid transparent; border-top: 5px solid var(--white); }

  .hero { position: absolute; left: 38px; top: 185px; width: 1122px; height: 535px; overflow: hidden; }
  .hero-photo {
    position: absolute; inset: 0;
    background: linear-gradient(90deg, #c9a062 0%, #b88a4e 22%, var(--wood-mid) 36%, var(--wood-light) 55%, var(--wood-mid) 75%, var(--wood-dark) 100%);
  }
  .hero-title { position: absolute; top: 118px; width: 100%; text-align: center; font-size: 62px; font-weight: 400; color: #000; }
  .hero-caption {
    position: absolute; left: 113px; top: 221px; width: 897px; height: 97px;
    background: rgba(255,255,255,0.45); border-radius: 4px;
    font-size: 19.5px; line-height: 28px; text-align: center; padding-top: 20px; color: #000;
  }
  .hero-cta {
    position: absolute; left: 470px; top: 358px; width: 183px; height: 57px; background: var(--white);
    font-size: 16px; font-weight: 700; text-align: center; line-height: 57px; color: #000;
  }
  .hero-controls { position: absolute; top: 479px; width: 100%; display: flex; justify-content: center; gap: 34px; font-size: 16px; font-weight: 700; color: #000; }

  .products-heading {
    position: absolute; top: 776px; width: 1200px; display: flex; justify-content: center; align-items: center; gap: 12px;
    font-size: 21px; font-weight: 700; color: #222;
  }
  .heading-square { width: 24px; height: 24px; border: 1.5px solid #222; }
  .product-list { position: absolute; top: 842px; left: 0; width: 1200px; }
  .product-photo {
    position: absolute; top: 0; width: 38px; height: 170px;
    background: linear-gradient(180deg, var(--product-wood) 0%, #5a2a18 18%, #3a2a22 30%, #3a2a22 100%);
    border-radius: 4px 4px 0 0;
  }
</style>
</head>
<body>
  <header class="site-header">
    <div class="brand-name">VELVET ORRA</div>
    <div class="search-form">
      <div class="search-field">Search</div>
      <div class="search-button">
        <svg width="17" height="17" viewBox="0 0 17 17"><circle cx="7" cy="7" r="5" fill="none" stroke="#fff" stroke-width="2.6"/><line x1="10.5" y1="10.5" x2="15" y2="15" stroke="#fff" stroke-width="3" stroke-linecap="round"/></svg>
      </div>
    </div>
    <svg class="account-icon" width="19" height="19" viewBox="0 0 19 19"><circle cx="9.5" cy="5" r="4.5" fill="var(--icon-blue)"/><path d="M1 19 C1 12 4 10.5 9.5 10.5 C15 10.5 18 12 18 19 Z" fill="var(--icon-blue)"/></svg>
    <svg class="cart-icon" width="22" height="19" viewBox="0 0 22 19"><path d="M0 1.5 H4 L7 12 H18 L20.5 4 H5.5" fill="none" stroke="var(--icon-blue)" stroke-width="2.6" stroke-linejoin="round"/><path d="M6 4 H20 L18 11 H8 Z" fill="var(--icon-blue)"/><circle cx="8.5" cy="16.5" r="2" fill="var(--icon-blue)"/><circle cx="16.5" cy="16.5" r="2" fill="var(--icon-blue)"/></svg>
    <div class="cart-count">0</div>
  </header>

  <nav class="main-nav">
    <a href="#">Musical Instruments <span class="caret"></span></a>
    <a href="#">Crystals<span class="caret"></span></a>
    <a href="#">Numismatic Collectibles</a>
    <a href="#">Cultural Artifacts</a>
    <a href="#">Blog</a>
    <a href="#">About Us</a>
    <a href="#">Contact Us</a>
  </nav>

  <section class="hero">
    <div class="hero-photo" role="img" aria-label="Acoustic guitar lying on dark weathered wooden planks"></div>
    <h1 class="hero-title">Musical Instruments</h1>
    <p class="hero-caption">Our guitars and other musical instruments would satisfy your auditory, tactile, kinesthetic<br>and visual perceptual channels.</p>
    <div class="hero-cta">Find out more</div>
    <div class="hero-controls"><span>Previous</span><span>Next</span></div>
  </section>

  <h2 class="products-heading"><span class="heading-square"></span>Some Products<span class="heading-square"></span></h2>

  <div class="product-list">
    <div class="product-photo" style="left:156px" role="img" aria-label="Acoustic guitar product photo"></div>
    <div class="product-photo" style="left:439px" role="img" aria-label="Acoustic guitar product photo"></div>
    <div class="product-photo" style="left:722px" role="img" aria-label="Acoustic guitar product photo"></div>
    <div class="product-photo" style="left:1005px" role="img" aria-label="Acoustic guitar product photo"></div>
  </div>
</body>
</html>
```